Personal Injury Funding Flyer

We are Qorvale Financial, a provider of receivables management solutions to the surgical industry.
We want a 1 page flyer to showcase our Motor Vehicle Accident (MVA) and Personal Injury (PI) case management and lien purchasing.

Attached is a document:
1- a flyer from a competitor. We like the overall feel of the flyer and the simplicity of the information presented.

You can also check out our website for examples of our company's style
www.qorvalefinancial.example

Target Market(s)

Surgeons, office managers, administrators and CFOS at smaller surgical facilities and surgical hospitals nationwide

Industry/Entity Type

Financial

Requirements
Must have
• Titled: Personal Injury Case Funding
• Tagline: We Ensure Your Cases are Financially Sound
• Include Qorvale Financial's logo
• Be sure to boldly highlight the 3 points:
• 3 Steps to Successful PI Case Management
• 1) Evaluate Cases
• Evaluate the financial aspects of the case including policy limits.
• 2) Consult Attorneys
• Evaluate the case background and likelihood of settlement.
• 3) Guaranteed Funding
• 15 day funding on most cases.
• How Does MVA/PI Funding Work?
• We pay you upfront and wait for the case to settle.
• Our funding eliminates the risk, hassle and uncertainty associated with PI cases.
• You get paid 100% NON-RECOURSE
• Include contact phone number (800) 555-0147
• >No Hassles
• >No Risk
• >Guaranteed Funds.
Nice to have
• Smiling doctor picture
Should not have
• Too much information

```html
<!DOCTYPE html>
<html lang="en">
<head>
<meta charset="utf-8">
<title>Qorvale Financial – Personal Injury Case Funding</title>
<link href="https://fonts.googleapis.com/css2?family=PT+Sans+Narrow:wght@400;700&family=PT+Sans:wght@700&display=swap" rel="stylesheet">
<style>
  :root {
    --paper: #ebebee;
    --navy: #13133d;
    --maroon: #5c1212;
    --grey: #8a8a8e;
    --photo-light: #f2f4f7;
    --photo-mid: #c9ced6;
  }
  * { margin: 0; padding: 0; box-sizing: border-box; }
  html, body { width: 1017px; height: 1200px; overflow: hidden; }
  body {
    background: var(--paper);
    font-family: "PT Sans Narrow", "Arial Narrow", sans-serif;
    color: var(--navy);
    position: relative;
  }
  .brand {
    position: absolute;
    display: flex;
    align-items: center;
    z-index: 2;
  }
  .brand-name {
    font-family: "PT Sans Narrow", sans-serif;
    font-weight: 700;
    color: var(--navy);
    white-space: nowrap;
  }
  .brand-mark { background: var(--maroon); flex: none; }
  .brand-divider { width: 1px; background: #bbb; }
  .brand-line {
    font-family: "PT Sans Narrow", sans-serif;
    font-weight: 700;
    color: var(--maroon);
    line-height: 1.05;
  }
  .brand--top { top: 48px; left: 135px; gap: 18px; }
  .brand--top .brand-mark { width: 42px; height: 42px; }
  .brand--top .brand-name { font-size: 62px; }
  .brand--top .brand-divider { height: 88px; margin: 0 8px; }
  .brand--top .brand-line { font-size: 27px; }
  .brand--bottom { top: 1090px; left: 165px; gap: 10px; }
  .brand--bottom .brand-mark { width: 20px; height: 20px; }
  .brand--bottom .brand-name { font-size: 30px; }
  .brand--bottom .brand-divider { height: 42px; margin: 0 4px; }
  .brand--bottom .brand-line { font-size: 13px; }

  .title {
    position: absolute; top: 178px; left: 0; width: 100%;
    text-align: center;
    font-family: "PT Sans", sans-serif;
    font-weight: 700; font-size: 44px; color: var(--navy);
  }
  .tagline {
    position: absolute; top: 278px; left: 0; width: 100%;
    text-align: center;
    font-weight: 700; font-size: 38px; color: var(--grey);
  }
  .steps-heading {
    position: absolute; top: 383px; left: 95px;
    font-weight: 700; font-size: 31px; color: var(--maroon);
  }
  .info { position: absolute; left: 95px; top: 458px; width: 520px; z-index: 2; }
  .label { font-weight: 700; font-size: 23px; color: var(--grey); line-height: 1.2; }
  .detail { font-weight: 700; font-size: 18px; color: var(--navy); line-height: 1.25; margin-top: 6px; }
  .step { margin-bottom: 12px; }
  .how { margin-top: 34px; }
  .how .detail { margin-top: 12px; }
  .recourse { margin-top: 18px; }
  .benefits { list-style: none; margin-top: 22px; font-weight: 700; font-size: 24px; color: var(--navy); line-height: 1.28; }
  .call {
    position: absolute; top: 1012px; left: 95px;
    font-family: "PT Sans", sans-serif;
    font-weight: 700; font-size: 40px; color: var(--navy);
    white-space: nowrap;
    z-index: 2;
  }
  .doctor-photo {
    position: absolute; left: 490px; top: 610px; width: 527px; height: 590px;
    z-index: 1;
    background: radial-gradient(ellipse at 58% 30%, var(--photo-mid) 0%, var(--photo-light) 55%, var(--paper) 80%),
                linear-gradient(180deg, var(--photo-light), var(--photo-mid));
  }
</style>
</head>
<body>
  <header class="brand brand--top">
    <span class="brand-mark"></span>
    <span class="brand-name">Qorvale Financial</span>
    <span class="brand-divider"></span>
    <span class="brand-line">Receivable<br>Management<br>Solutions</span>
  </header>

  <h1 class="title">Personal Injury Case Funding</h1>
  <p class="tagline">“We Ensure Your Cases are Financially Sound”</p>
  <h2 class="steps-heading">3 Steps to Successful PI Case Management</h2>

  <section class="info">
    <div class="step">
      <p class="label">Evaluate Cases</p>
      <p class="detail">Evaluate the financial aspects of the case including policy limits.</p>
    </div>
    <div class="step">
      <p class="label">Consult Attorneys</p>
      <p class="detail">Evaluate the case background and likelihood of settlement.</p>
    </div>
    <div class="step">
      <p class="label">Guaranteed Funding</p>
      <p class="detail">15 day funding on most cases.</p>
    </div>
    <div class="how">
      <p class="label">How Does MVA/PI Funding Work?</p>
      <p class="detail">We pay you upfront and wait for the case to settle.</p>
      <p class="detail">Our funding eliminates the risk, hassle and uncertainty<br>associated with PI cases.</p>
    </div>
    <p class="label recourse">You get paid 100% NON-RECOURSE</p>
    <ul class="benefits">
      <li>No Risk</li>
      <li>No Hassles</li>
      <li>Guaranteed Funds.</li>
    </ul>
  </section>

  <p class="call">Call Us: (800) 555-0147</p>

  <footer class="brand brand--bottom">
    <span class="brand-mark"></span>
    <span class="brand-name">Qorvale Financial</span>
    <span class="brand-divider"></span>
    <span class="brand-line">Receivable<br>Management<br>Solutions</span>
  </footer>

  <div class="doctor-photo" role="img" aria-label="Photo of a smiling doctor in a white coat with a stethoscope"></div>
</body>
</html>
```